Candy Packaging

I'm looking for a logo design for a confectionary company called Gran's Sweet Delights.
Something that will be appealing to women.
The packaging in interested in will be a stand up guseted bag with a window.
Dimensions ar 7 1/2in high, 4in wide 2in thick.

Im trying to upload pictures of the product and I'm not sure if the're loading.

Target Market(s)

Adult Females

Industry/Entity Type

It Company

```html
<!DOCTYPE html>
<html lang="en">
<head>
<meta charset="UTF-8">
<title>Gran's Sweet Delights – Almond Crunch Bag Front</title>
<link rel="stylesheet" href="https://fonts.googleapis.com/css2?family=Lora:wght@400&display=swap">
<style>
  :root {
    --page-bg: #ffffff;
    --bag-yellow: #e6df7d;
    --seal-yellow: #e3dc78;
    --stripe-white: #ffffff;
    --ink-blue: #1c35a6;
    --ink-black: #1a1a1a;
    --window-light: #d3d0a4;
    --window-dark: #aeac84;
  }
  * { margin: 0; padding: 0; box-sizing: border-box; }
  html, body {
    width: 900px;
    height: 1200px;
    overflow: hidden;
    background: var(--page-bg);
  }
  .canvas {
    position: relative;
    width: 900px;
    height: 1200px;
  }
  .bag-front {
    position: absolute;
    left: 230px;
    top: 170px;
    width: 440px;
    height: 850px;
  }
  .top-seal {
    position: absolute;
    left: 0;
    top: 0;
    width: 100%;
    height: 46px;
    background: var(--seal-yellow);
    box-shadow: inset 0 -2px 0 rgba(0,0,0,0.05);
  }
  .striped-panel {
    position: absolute;
    left: 0;
    top: 46px;
    width: 100%;
    height: 804px;
    background: repeating-linear-gradient(
      90deg,
      var(--bag-yellow) 0px,
      var(--bag-yellow) 13px,
      var(--stripe-white) 13px,
      var(--stripe-white) 17px
    );
  }
  .brand-name {
    position: absolute;
    left: 0;
    top: 150px;
    width: 100%;
    text-align: center;
    font-family: "Lora", Georgia, serif;
    font-weight: 400;
    font-size: 36px;
    line-height: 1.2;
    color: var(--ink-black);
  }
  .product-window {
    position: absolute;
    left: 112px;
    top: 300px;
    width: 200px;
    height: 320px;
  }
  .product-window svg {
    display: block;
    width: 100%;
    height: 100%;
  }
  .product-name {
    position: absolute;
    left: 0;
    top: 646px;
    width: 100%;
    text-align: center;
    font-family: "Lora", Georgia, serif;
    font-weight: 400;
    font-size: 19px;
    color: var(--ink-blue);
    letter-spacing: 0.5px;
  }
  .net-weight {
    position: absolute;
    left: 0;
    top: 706px;
    width: 100%;
    text-align: center;
    font-family: "Lora", Georgia, serif;
    font-size: 15px;
    color: var(--ink-black);
  }
</style>
</head>
<body>
  <main class="canvas">
    <section class="bag-front" aria-label="Front panel of stand-up gusseted candy bag">
      <div class="top-seal"></div>
      <div class="striped-panel">
        <h1 class="brand-name">Gran's Sweet Delights</h1>

        <div class="product-window" role="img" aria-label="Clear window showing pieces of almond crunch inside the bag">
          <svg viewBox="0 0 200 320" xmlns="http://www.w3.org/2000/svg" aria-hidden="true">
            <defs>
              <linearGradient id="window-fill" x1="0" y1="0" x2="1" y2="1">
                <stop offset="0" stop-color="#d3d0a4"/>
                <stop offset="1" stop-color="#aeac84"/>
              </linearGradient>
            </defs>
            <path d="M18 8
                     C 55 0, 78 20, 102 33
                     C 126 45, 156 43, 177 18
                     C 190 4, 200 20, 200 40
                     L 200 284
                     C 200 308, 186 320, 166 320
                     L 30 320
                     C 10 320, 0 308, 0 288
                     L 0 30
                     C 0 16, 8 10, 18 8 Z"
                  fill="url(#window-fill)"/>
          </svg>
        </div>

        <p class="product-name">Golden Almond Crunch</p>
        <p class="net-weight">120g</p>
      </div>
    </section>
  </main>
</body>
</html>
```